Lift-Lark needs a design for a new mobile app

A new app - lift-lark.example, requires a design for its new app.

The app lets users add, create and share gym sessions. Sessions can be created, sets added and exercises chosen.

The app is currently functional on Android only (ios later), all that is required is a design for the app.

Some design assets are available (logo, colours, font), so the app should tie into these.

The design needs to be clean, simple and obvious, and all design assets will be required as part of this project.

One of the pages has % complete on the set - an icon to demonstrate this rather than a text based (eg 50%) would be great.

Screenshots will be available, along with the logos, colours and fonts.

Target Market(s)

Gym goers, all ages, male & female, fitness enthusiasts
Users of phones and tablets

Industry/Entity Type

Gym

Requirements
Must have
• Designs examples for each of the screens in the app, and an obvious selection of reusable elements (such as drop downs, radio buttons, buttons, calendar selectors, check boxes etc)
• Colours, logos and branding to fit into what is already available on the website.
• Usability and consistency are vital. Buttons should be in the same place (where possible).
• Design should help the user to complete the journey, and not get in the way.
• It should be a pleasure to use the app.
• Happy to have white space where appropriate.
• We use native elements where available.
Should not have
• Design features that waste space

```html
<!DOCTYPE html>
<html lang="en">
<head>
<meta charset="UTF-8">
<title>Lift-Lark — Navigation Drawer</title>
<link href="https://fonts.googleapis.com/css2?family=Roboto:wght@400;500;700&display=swap" rel="stylesheet">
<style>
  :root{
    --brand:#6473d6;
    --brand-panel:#6b78da;
    --brand-ring:#8c97e6;
    --band:#a7aee8;
    --accent:#d56fd0;
    --ink:#222222;
    --muted:#8a8a8a;
    --rule:#9a9a9a;
    --white:#ffffff;
    --photo-a:#b9a48f;
    --photo-b:#5d6a7f;
  }
  *{margin:0;padding:0;box-sizing:border-box}
  html,body{width:675px;height:1200px;overflow:hidden;background:var(--white)}
  body{font-family:'Roboto',Arial,sans-serif;position:relative}
  .screen{position:absolute;inset:0;overflow:hidden}

  /* underlying calendar screen */
  .calendar{position:absolute;left:570px;top:0;width:105px;height:1200px;background:var(--white);overflow:hidden}
  .calendar-head{position:absolute;left:0;top:0;width:105px;height:669px;background:var(--brand-panel)}
  .hamburger{position:absolute;left:36px;top:86px}
  .weekday{position:absolute;left:49px;top:168px;transform:translateX(-50%);color:var(--white);font-size:21px;font-weight:500}
  .day{position:absolute;left:49px;transform:translate(-50%,-50%);color:var(--white);font-size:23px}
  .day.past{color:rgba(255,255,255,.55)}
  .day-today{position:absolute;left:17px;top:270px}
  .day-event{position:absolute;left:29px;top:492px;width:40px;height:40px;border-radius:50%;background:var(--accent)}
  .hint{position:absolute;left:30px;top:576px;color:rgba(255,255,255,.85);font-size:21px;line-height:25px;white-space:nowrap}
  .date-band{position:absolute;left:0;top:669px;width:105px;height:81px;background:var(--band);color:var(--white);font-size:29px;padding:24px 0 0 30px;white-space:nowrap}
  .session{position:absolute;left:0;width:105px;white-space:nowrap}
  .session-icon{position:absolute;left:36px;width:26px;height:36px;border-radius:5px;background:#1f1f1f}
  .session-title{position:absolute;left:96px;font-size:25px;color:var(--ink)}
  .session-meta{position:absolute;left:96px;font-size:18px;line-height:23px;color:var(--muted)}

  /* status bar */
  .status{position:absolute;left:0;top:0;width:675px;height:45px;z-index:3}
  .status-time{position:absolute;right:18px;top:11px;color:var(--white);font-size:22px;font-weight:500}
  .status-icons{position:absolute;left:492px;top:10px}

  /* drawer */
  .drawer{position:absolute;left:0;top:0;width:570px;height:1200px;background:var(--white);box-shadow:6px 0 18px rgba(0,0,0,.22);z-index:2}
  .drawer-head{position:absolute;left:0;top:0;width:570px;height:405px;background:var(--brand)}
  .notch{position:absolute;left:264px;top:384px}
  .head-action{position:absolute;top:128px}
  .head-action.power{left:94px}
  .head-action.settings{left:430px}
  .avatar-ring{position:absolute;left:216px;top:81px;width:138px;height:138px;border-radius:50%;background:var(--brand-ring)}
  .avatar{position:absolute;left:225px;top:90px;width:120px;height:120px;border-radius:50%;background:linear-gradient(160deg,var(--photo-a),var(--photo-b))}
  .profile-name{position:absolute;left:0;top:238px;width:570px;text-align:center;color:var(--white);font-size:30px;font-weight:700}
  .profile-role{position:absolute;left:0;top:286px;width:570px;text-align:center;color:var(--white);font-size:22px;font-weight:500;line-height:28px}

  .menu{position:absolute;left:0;top:0;width:570px;list-style:none}
  .menu-item{position:absolute;left:0;width:570px;text-align:center;color:var(--ink);font-size:26px;transform:translateY(-50%)}
  .divider{position:absolute;left:37px;top:1081px;width:496px;height:2px;background:var(--rule)}
  .share-row{position:absolute;left:0;top:1140px;width:570px}
  .share-link{position:absolute;transform:translate(-50%,-50%);color:var(--ink);font-size:24px;font-weight:700}
  .share-mail{position:absolute;left:406px;top:1126px}
</style>
</head>
<body>
<div class="screen">

  <section class="calendar">
    <div class="calendar-head"></div>
    <svg class="hamburger" width="36" height="24" viewBox="0 0 36 24"><rect y="0" width="36" height="4" fill="#fff"/><rect y="10" width="36" height="4" fill="#fff"/><rect y="20" width="36" height="4" fill="#fff"/></svg>
    <div class="weekday">SUN</div>
    <div class="day past" style="top:238px">30</div>
    <svg class="day-today" width="64" height="64" viewBox="0 0 64 64">
      <circle cx="32" cy="32" r="29" fill="none" stroke="#fff" stroke-width="3" stroke-dasharray="120 12 30 20"/>
      <circle cx="32" cy="32" r="20" fill="#fff"/>
      <text x="32" y="40" text-anchor="middle" font-family="Roboto,Arial,sans-serif" font-size="22" fill="#6473d6">6</text>
    </svg>
    <div class="day" style="top:375px">13</div>
    <div class="day" style="top:444px">20</div>
    <div class="day-event"></div>
    <div class="day" style="top:512px">27</div>
    <div class="hint">Select a day<br>create new</div>
    <div class="date-band">6 May</div>
    <div class="session" style="top:775px">
      <div class="session-icon" style="top:0" role="img" aria-label="Treadmill exercise icon"></div>
      <div class="session-title" style="top:0">Cardio</div>
      <div class="session-meta" style="top:34px">10 min run</div>
    </div>
    <div class="session" style="top:885px">
      <div class="session-icon" style="top:8px" role="img" aria-label="Dumbbell exercise icon"></div>
      <div class="session-title" style="top:0">Hips</div>
      <div class="session-meta" style="top:34px">5 x 12<br>5 x 10<br>7 x 8</div>
    </div>
    <div class="session" style="top:1056px">
      <div class="session-icon" style="top:8px" role="img" aria-label="Dumbbell exercise icon"></div>
      <div class="session-title" style="top:0">Biceps</div>
      <div class="session-meta" style="top:34px">6 x 12<br>6 x 10<br>6 x 8</div>
    </div>
  </section>

  <div class="status">
    <svg class="status-icons" width="104" height="26" viewBox="0 0 104 26">
      <path d="M0 6 Q15 -4 30 6 L15 24 Z" fill="#fff"/>
      <path d="M38 24 L60 2 L60 24 Z" fill="#fff"/>
      <rect x="72" y="2" width="13" height="22" rx="1.5" fill="#fff"/>
    </svg>
    <div class="status-time">15:30</div>
  </div>

  <nav class="drawer">
    <header class="drawer-head">
      <svg class="head-action power" width="44" height="44" viewBox="0 0 44 44">
        <path d="M13 10 A15 15 0 1 0 31 10" fill="none" stroke="#fff" stroke-width="4" stroke-linecap="round"/>
        <line x1="22" y1="3" x2="22" y2="21" stroke="#fff" stroke-width="4" stroke-linecap="round"/>
      </svg>
      <div class="avatar-ring"></div>
      <div class="avatar" role="img" aria-label="Profile photo of the trainer"></div>
      <svg class="head-action settings" width="44" height="44" viewBox="0 0 44 44">
        <g fill="#fff">
          <circle cx="22" cy="22" r="14"/>
          <rect x="18" y="2" width="8" height="40" rx="1.5"/>
          <rect x="18" y="2" width="8" height="40" rx="1.5" transform="rotate(45 22 22)"/>
          <rect x="18" y="2" width="8" height="40" rx="1.5" transform="rotate(90 22 22)"/>
          <rect x="18" y="2" width="8" height="40" rx="1.5" transform="rotate(135 22 22)"/>
        </g>
        <circle cx="22" cy="22" r="6" fill="#6473d6"/>
      </svg>
      <div class="profile-name">Dani Kusuma</div>
      <div class="profile-role">Personal Gym Trainer<br>(Lift-Lark.example)</div>
      <svg class="notch" width="42" height="22" viewBox="0 0 42 22"><path d="M0 21 L21 0 L42 21 Z" fill="#fff"/></svg>
    </header>

    <ul class="menu">
      <li class="menu-item" style="top:478px">Calendar</li>
      <li class="menu-item" style="top:566px">Community</li>
      <li class="menu-item" style="top:654px">Notification</li>
      <li class="menu-item" style="top:743px">Export Session</li>
      <li class="menu-item" style="top:831px">Upload Training</li>
      <li class="menu-item" style="top:919px">Share this app</li>
      <li class="menu-item" style="top:1007px">Rate this app</li>
    </ul>

    <div class="divider"></div>
    <div class="share-row">
      <span class="share-link" style="left:146px;top:0">Friendly</span>
      <span class="share-link" style="left:285px;top:0">Chirper</span>
    </div>
    <svg class="share-mail" width="40" height="30" viewBox="0 0 40 30">
      <rect x="0" y="0" width="40" height="30" rx="2" fill="#111"/>
      <path d="M4 5 L20 16 L36 5" fill="none" stroke="#fff" stroke-width="3"/>
    </svg>
  </nav>

</div>
</body>
</html>
```